Company Values One-Pager

We're a recruitment firm based in Singapore, focused on the startup tech and VC sectors. www.brelvanhire.com

As we're now at the point of growing and hiring, we want a one-pager (PDF or whatever) that summarises us and our company values.

I've attached a short PowerPoint that goes into the values etc.

Font styles to use
Sans Serif

Requirements
Must have
• We like a 'clean' look. Our logo is bright and simple, and that's what we're looking for.
• The official colour code for the logo is seafoam green
• www.huepondlab.com/color/71EEB8/sea_foam_green
• Our website also gives a good insight.
• I'd like logos that summarise each value alongside them. i.e + for positivity, a letter for delivery etc. (Just ideas - please innovate!)
Should not have
• Nothing dark - just keep it simple and fresh

```html
<!DOCTYPE html>
<html lang="en">
<head>
<meta charset="utf-8">
<title>Brelvan Hire – Our Values</title>
<link rel="stylesheet" href="https://fonts.googleapis.com/css2?family=Lato:wght@700;900&display=swap">
<style>
  :root {
    --green: #6aae94;
    --grey: #8a8a8a;
    --paper: #ffffff;
  }
  html, body {
    margin: 0;
    padding: 0;
    width: 849px;
    height: 1200px;
    overflow: hidden;
    background: var(--paper);
  }
  .page {
    position: relative;
    width: 849px;
    height: 1200px;
    font-family: "Lato", Arial, sans-serif;
  }
  .page-frame {
    position: absolute;
    left: 20px;
    top: 23px;
    width: 801px;
    height: 1148px;
    border: 4px solid var(--grey);
  }
  .brand {
    position: absolute;
    left: 36px;
    top: 92px;
    display: flex;
    align-items: center;
    gap: 12px;
    background: var(--paper);
    padding: 6px 8px;
  }
  .brand-square {
    width: 16px;
    height: 16px;
    background: var(--green);
  }
  .brand-name {
    color: var(--green);
    font-weight: 700;
    font-size: 30px;
    letter-spacing: 3px;
  }
  .title {
    position: absolute;
    top: 200px;
    left: 0;
    width: 849px;
    margin: 0;
    text-align: center;
    font-weight: 900;
    font-size: 80px;
    line-height: 1;
    letter-spacing: 1px;
    color: var(--grey);
  }
  .title .accent { color: var(--green); }
  .values {
    position: absolute;
    left: 0;
    top: 0;
    width: 849px;
    height: 1200px;
  }
  .value-frame {
    fill: none;
    stroke: var(--green);
    stroke-width: 4.5;
  }
  .value-label {
    font-family: "Lato", Arial, sans-serif;
    font-weight: 900;
    font-size: 16.5px;
    fill: var(--grey);
  }
  .icon-green { fill: var(--green); }
  .icon-grey { fill: var(--grey); }
  .speed-line { stroke: var(--green); stroke-width: 2; }
  .site {
    position: absolute;
    bottom: 54px;
    left: 0;
    width: 849px;
    text-align: center;
    font-weight: 900;
    font-size: 24px;
    color: var(--grey);
  }
  .site .accent { color: var(--green); }
</style>
</head>
<body>
<div class="page">
  <div class="page-frame"></div>

  <div class="brand">
    <span class="brand-square"></span>
    <span class="brand-name">BRELVAN HIRE</span>
  </div>

  <h1 class="title">OUR <span class="accent">VALUES</span></h1>

  <svg class="values" viewBox="0 0 595 842" aria-label="Company values: positivity, proactivity, teamwork, delivery">
    <!-- positivity -->
    <path class="value-frame" d="M300 330 V297 H152 V446 H293"/>
    <text class="value-label" x="172" y="354">POSITIVITY</text>
    <circle class="icon-green" cx="226" cy="393" r="17"/>

    <!-- proactivity -->
    <path class="value-frame" d="M293 440 V362 H443 V508 H300"/>
    <text class="value-label" x="305" y="411">PROACTIVITY</text>
    <circle class="icon-grey" cx="323" cy="453" r="8"/>
    <circle class="icon-grey" cx="345" cy="453" r="8"/>
    <circle class="icon-green" cx="369" cy="453" r="14"/>
    <circle class="icon-grey" cx="392" cy="453" r="8"/>
    <circle class="icon-grey" cx="414" cy="453" r="8"/>

    <!-- teamwork -->
    <path class="value-frame" d="M300 510 V479 H152 V625 H293"/>
    <text class="value-label" x="167" y="530">TEAMWORK</text>
    <circle class="icon-green" cx="180" cy="570" r="9.5"/>
    <circle class="icon-green" cx="203" cy="570" r="9.5"/>
    <circle class="icon-green" cx="226" cy="570" r="9.5"/>
    <circle class="icon-green" cx="249" cy="570" r="9.5"/>
    <circle class="icon-green" cx="272" cy="570" r="9.5"/>

    <!-- delivery -->
    <path class="value-frame" d="M293 600 V540 H443 V688 H295 V652"/>
    <text class="value-label" x="322" y="592">DELIVERY</text>
    <line class="speed-line" x1="338" y1="619" x2="368" y2="619"/>
    <line class="speed-line" x1="342" y1="624" x2="366" y2="624"/>
    <line class="speed-line" x1="346" y1="629" x2="366" y2="629"/>
    <line class="speed-line" x1="350" y1="634" x2="366" y2="634"/>
    <line class="speed-line" x1="354" y1="639" x2="368" y2="639"/>
    <line class="speed-line" x1="358" y1="644" x2="370" y2="644"/>
    <circle class="icon-green" cx="382" cy="632" r="18"/>
  </svg>

  <div class="site">www.brelvan<span class="accent">hire</span>.com</div>
</div>
</body>
</html>
```